Retail Package Design for Consumer Product Goods (soup)

Company is in need of food package design (front and back). Product will be in a stand-up pouch-type packaging. Size is 10.4 inch (vertical) by 7.65 inch (horizontal). Product is for retail sales, so design needs to be eye catching. It's considered more healthy food, so would like the design to be communicate health.
Target Market(s)
Natural healthy food
Industry/Entity Type
Retail
Requirements
Must have
- Must be done in Illustrator.
FRONT:
Clean, simple design that communicates premium and healthy food. Name of Product is "Duck & Barley Soup" with subtitle of "Made with Organic Seaweed"
- Callouts somewhere on the package: "Traditional Korean-Style Soup", "Fully Cooked, Ready in Minutes", and "Beef used raised with no hormones & antibiotics".
- Bottom of package should say "Net Wt. 2 LBs (32oz)" and "Keep Refrigerated".
BACKSIDE
- See attached document "Content for Backside" for content: Nutrition Fact, Ingredient List, Place for a bar code, brief summary of the product
Nice to have
- would like to see rendering of pouch

```html
<!DOCTYPE html>
<html lang="en">
<head>
<meta charset="utf-8">
<title>Duck &amp; Barley Soup – Pouch Front</title>
<link href="https://fonts.googleapis.com/css2?family=Rye&family=Permanent+Marker&family=Montserrat:wght@500;700&family=Bebas+Neue&display=swap" rel="stylesheet">
<style>
  :root {
    --white: #ffffff;
    --red: #c11d2a;
    --red-light: #d9535d;
    --green: #1f5a22;
    --green-dark: #0f3d14;
    --gold: #f5b325;
    --yellow-text: #f6c94a;
    --badge: #f4d27a;
    --icon-green: #5faa44;
    --label-text: #d9e6d4;
  }
  * { margin: 0; padding: 0; box-sizing: border-box; }
  html, body { width: 1102px; height: 1200px; overflow: hidden; background: var(--white); }
  .pouch-front { position: relative; width: 1102px; height: 1200px; background: var(--white); }

  .brand {
    position: absolute; top: 110px; left: 0; width: 100%;
    display: flex; justify-content: center; align-items: center; gap: 14px;
    font-family: "Montserrat", sans-serif; font-weight: 700; font-size: 34px; color: var(--red);
  }
  .brand-dot { width: 26px; height: 26px; border-radius: 50%; background: var(--red); }

  .bands { position: absolute; inset: 0; }

  .product-name {
    position: absolute; top: 300px; left: 0; width: 100%; text-align: center;
    font-family: "Rye", serif; font-size: 92px; color: var(--white);
    text-shadow: 3px 4px 4px rgba(80,0,0,.55); letter-spacing: 1px;
  }
  .product-type {
    position: absolute; top: 428px; left: 0; width: 100%;
    display: flex; justify-content: center; align-items: center; gap: 22px;
    font-family: "Permanent Marker", cursive; font-size: 84px; color: var(--white);
    text-shadow: 2px 3px 3px rgba(80,0,0,.45);
  }
  .product-type::before, .product-type::after {
    content: ""; width: 90px; height: 5px; background: var(--white);
  }

  .subtitle {
    position: absolute; top: 600px; left: 110px;
    font-family: "Montserrat", sans-serif; font-weight: 700; font-size: 52px; line-height: 1.2;
    color: var(--yellow-text);
  }

  .serving-photo {
    position: absolute; left: 520px; top: 575px; width: 480px; height: 380px;
    border-radius: 50% 50% 48% 48% / 40% 40% 60% 60%;
    background: radial-gradient(ellipse at 50% 32%, #5e6648 0%, #4a4d36 30%, #e9eaea 46%, #ffffff 60%, #e2e4e4 100%);
  }

  .callouts {
    position: absolute; top: 970px; left: 95px; width: 620px;
    display: flex; justify-content: space-between;
  }
  .callout { width: 180px; text-align: center; }
  .callout svg { display: block; margin: 0 auto 14px; }
  .callout-text {
    font-family: "Montserrat", sans-serif; font-weight: 500; font-size: 15px; line-height: 1.3; color: var(--label-text);
  }

  .net-weight {
    position: absolute; top: 962px; left: 815px; width: 112px; height: 146px;
    background: var(--badge); padding-top: 8px; text-align: center;
    font-family: "Bebas Neue", sans-serif; color: var(--green); font-size: 40px; line-height: 1;
  }
  .storage {
    position: absolute; top: 1120px; left: 760px; width: 222px; text-align: center;
    font-family: "Montserrat", sans-serif; font-weight: 700; font-size: 18px; color: var(--white);
  }
</style>
</head>
<body>
<main class="pouch-front">
  <svg class="bands" width="1102" height="1200" viewBox="0 0 1102 1200" aria-hidden="true">
    <defs>
      <radialGradient id="redGlow" cx="50%" cy="35%" r="65%">
        <stop offset="0" stop-color="var(--red-light)"/>
        <stop offset="1" stop-color="var(--red)"/>
      </radialGradient>
      <linearGradient id="greenShade" x1="0" y1="0" x2="0" y2="1">
        <stop offset="0" stop-color="var(--green-dark)"/>
        <stop offset="1" stop-color="var(--green)"/>
      </linearGradient>
    </defs>
    <path d="M0 230 Q551 330 1102 230 L1102 920 Q551 840 0 920 Z" fill="url(#redGlow)"/>
    <path d="M0 230 Q551 330 1102 230" fill="none" stroke="var(--gold)" stroke-width="8"/>
    <path d="M0 920 Q551 840 1102 920 L1102 1160 L0 1160 Z" fill="url(#greenShade)"/>
    <path d="M0 920 Q551 840 1102 920" fill="none" stroke="var(--gold)" stroke-width="8"/>
  </svg>

  <div class="brand"><span class="brand-dot"></span>Warm Spoon Kitchen</div>

  <h1 class="product-name">Duck &amp; Barley</h1>
  <div class="product-type">SOUP</div>

  <p class="subtitle">Made<br>with<br>Organic<br>Seaweed</p>

  <div class="serving-photo" role="img" aria-label="Photo of a white bowl of duck and barley soup with seaweed"></div>

  <section class="callouts">
    <div class="callout">
      <svg width="90" height="90" viewBox="0 0 90 90" aria-hidden="true">
        <path d="M8 46 H72 Q70 80 40 80 Q10 80 8 46 Z" fill="var(--icon-green)"/>
        <path d="M50 56 L86 18 M58 60 L88 28" stroke="var(--icon-green)" stroke-width="4" stroke-linecap="round"/>
        <path d="M30 38 Q24 30 30 22 Q36 14 30 6 M42 38 Q36 30 42 22 Q48 14 42 6" fill="none" stroke="var(--icon-green)" stroke-width="3"/>
      </svg>
      <p class="callout-text">Traditional<br>Korean-Style Soup</p>
    </div>
    <div class="callout">
      <svg width="90" height="90" viewBox="0 0 90 90" aria-hidden="true">
        <circle cx="45" cy="50" r="33" fill="none" stroke="var(--icon-green)" stroke-width="7"/>
        <rect x="38" y="4" width="14" height="8" fill="var(--icon-green)"/>
        <path d="M14 20 L22 12 M76 20 L68 12" stroke="var(--icon-green)" stroke-width="6" stroke-linecap="round"/>
        <text x="45" y="59" text-anchor="middle" font-family="Bebas Neue, sans-serif" font-size="26" fill="var(--icon-green)">0:1</text>
      </svg>
      <p class="callout-text">Fully Cooked,<br>Ready in Minutes</p>
    </div>
    <div class="callout">
      <svg width="90" height="90" viewBox="0 0 90 90" aria-hidden="true">
        <circle cx="45" cy="45" r="36" fill="none" stroke="var(--icon-green)" stroke-width="5"/>
        <path d="M20 20 L70 70" stroke="var(--icon-green)" stroke-width="5"/>
        <rect x="30" y="34" width="30" height="14" rx="7" transform="rotate(-45 45 41)" fill="var(--icon-green)"/>
        <circle cx="48" cy="60" r="3" fill="var(--icon-green)"/>
        <circle cx="56" cy="56" r="3" fill="var(--icon-green)"/>
      </svg>
      <p class="callout-text">Beef used raised<br>with no hormones<br>&amp; antibiotics</p>
    </div>
  </section>

  <div class="net-weight">NET WT<br>2 LBS<br>(32OZ)</div>
  <p class="storage">Keep Refrigerated</p>
</main>
</body>
</html>
```